We are looking for a simple design that would be uplifting for
upscale drug addicts

MERIDIAN COLLECTIVE

PLEASE SEE THE LINK FOR TAG LINE AND CONTENT

thank you.

here is all the actual info we need and we want something like this...

http://files.qzr.lumtrabox.example/rest/objects/7c2910e4b557d81a93e40bd59fa644163fe2adf0899f?uid=bdf8e1b9b6f556b6b83c44471fdc79%2fproofs&expires=1482716603&signature=kT9PwLmQxZbVoNHLdtrtlmoGHQB%3d

The shape and colors don't have to be like what I posted it is only an example.

Target Market(s)

Harlow Row, internet and creative types, men, early 30's,
upwardly mobile, drug addicts

current site

brightkestrelway.example

now launching new name Meridian Collective

Industry/Entity Type

Drug

Requirements
Must have
• upscale look, great font
Should not have
• a corporate look but should not look like a clinic.

```html
<!DOCTYPE html>
<html lang="en">
<head>
<meta charset="utf-8">
<title>Meridian Collective – Business Card</title>
<link href="https://fonts.googleapis.com/css2?family=Roboto+Condensed:wght@400;500&display=swap" rel="stylesheet">
<style>
  :root {
    --stage: #ececec;
    --card-white: #ffffff;
    --brand-blue: #0090c4;
    --ink-blue: #0a8cc4;
    --on-blue: #ffffff;
    --shadow: rgba(0, 0, 0, 0.28);
  }
  * { box-sizing: border-box; margin: 0; padding: 0; }
  html, body {
    width: 1200px;
    height: 900px;
    overflow: hidden;
    background: var(--stage);
    font-family: "Roboto Condensed", "Arial Narrow", sans-serif;
  }
  .canvas {
    position: relative;
    width: 1200px;
    height: 900px;
  }
  .business-card {
    position: absolute;
    left: 100px;
    top: 171px;
    width: 1000px;
    height: 558px;
    display: flex;
    box-shadow: 0 18px 24px -14px var(--shadow);
  }
  .card-front {
    position: relative;
    width: 547px;
    height: 100%;
    background: var(--card-white);
  }
  .holder-name {
    position: absolute;
    right: 45px;
    top: 238px;
    font-size: 48px;
    font-weight: 400;
    line-height: 1.1;
    color: var(--ink-blue);
    letter-spacing: -0.5px;
    white-space: nowrap;
  }
  .holder-role {
    position: absolute;
    right: 55px;
    top: 296px;
    font-size: 28px;
    font-weight: 400;
    line-height: 1.1;
    color: var(--ink-blue);
    letter-spacing: -0.3px;
    white-space: nowrap;
  }
  .card-panel {
    position: relative;
    flex: 1;
    height: 100%;
    background: var(--brand-blue);
    color: var(--on-blue);
  }
  .perforation {
    position: absolute;
    left: 6px;
    top: 0;
    width: 2px;
    height: 100%;
  }
  .brand-name {
    position: absolute;
    left: 32px;
    top: 18px;
    font-size: 42px;
    font-weight: 400;
    line-height: 1.1;
    letter-spacing: -0.6px;
    white-space: nowrap;
  }
  .brand-tagline {
    position: absolute;
    left: 32px;
    top: 72px;
    width: 400px;
    font-size: 20px;
    line-height: 20px;
    letter-spacing: -0.2px;
  }
  .contact-row {
    position: absolute;
    left: 46px;
    display: flex;
    align-items: center;
    gap: 14px;
  }
  .contact-row svg { width: 36px; height: 36px; flex: none; }
  .contact-text {
    font-size: 21px;
    line-height: 25px;
    letter-spacing: -0.1px;
    white-space: nowrap;
  }
  .row-address { top: 332px; }
  .row-phone { top: 417px; }
  .row-email { top: 500px; }
</style>
</head>
<body>
<main class="canvas">
  <article class="business-card">
    <section class="card-front">
      <h1 class="holder-name">Daniel Corvan, CASAC</h1>
      <p class="holder-role">Program Coordinator</p>
    </section>
    <section class="card-panel">
      <svg class="perforation" viewBox="0 0 2 558" preserveAspectRatio="none" aria-hidden="true">
        <line x1="1" y1="0" x2="1" y2="558" stroke="#ffffff" stroke-width="2" stroke-dasharray="8 6"/>
      </svg>
      <h2 class="brand-name">MERIDIAN COLLECTIVE</h2>
      <p class="brand-tagline">We walk beside you every step of the way toward lasting recovery</p>

      <div class="contact-row row-address">
        <svg viewBox="0 0 36 36" aria-hidden="true" fill="none" stroke="#ffffff" stroke-width="1.6">
          <circle cx="18" cy="18" r="16.5"/>
          <path d="M9 17 L27 10 L20 27 L17 19 Z" stroke-linejoin="round"/>
        </svg>
        <p class="contact-text">418 Larkfield Ave. Suite 302<br>Brookhollow, NY 10482</p>
      </div>

      <div class="contact-row row-phone">
        <svg viewBox="0 0 36 36" aria-hidden="true" fill="none" stroke="#ffffff" stroke-width="1.6">
          <circle cx="18" cy="18" r="16.5"/>
          <path d="M12 10 C10 12 10 15 12 19 C14 23 17 26 21 27 C23 27.5 25 26 26 24 L22.5 21 L20.5 22.5 C18 21.5 15.5 19 14.5 16 L16 14 Z" stroke-linejoin="round"/>
        </svg>
        <p class="contact-text">555.014.2270<br>555.014.2271</p>
      </div>

      <div class="contact-row row-email">
        <svg viewBox="0 0 36 36" aria-hidden="true" fill="none" stroke="#ffffff" stroke-width="1.6">
          <circle cx="18" cy="18" r="16.5"/>
          <path d="M9 12 L18 20 L27 12 M9 12 L9 24 L27 24 L27 12" stroke-linejoin="round"/>
        </svg>
        <p class="contact-text">counselor@larkfieldcare.example</p>
      </div>
    </section>
  </article>
</main>
</body>
</html>
```